BrookfieldVentures Business Card Design

Design business cards with attached ideas. I am open to several different ideas that would be interesting and innovative. What I have provided is logo and colors. Font should be Helvetica although it could be bold or light as needed. The design can be vertical or horizontal. The design should be more interesting than a standard business card. Files must be ready to send to a printer and in Illustrator format. The text with the five icons should be exact. Send me some ideas and I will get back to you right away. I need to choose a design within 3-5 days.

Target Market(s)

Business audience

Industry/Entity Type

Business

Contact Information for Business Card

Files should be ready to send to printer in illustrator format

Font styles to use
Sans Serif

Colors
3276b5

Requirements
Must have
• Use attached logo and two colors - blue / gray
• Include 5 offering icons and text on back
Nice to have
• Interesting and innovative design. Vertical or horizontal are both fine.

```html
<!DOCTYPE html>
<html lang="en">
<head>
<meta charset="utf-8">
<title>BrookfieldVentures Business Card</title>
<link rel="stylesheet" href="https://fonts.googleapis.com/css2?family=Arimo:wght@400;700&display=swap">
<style>
  :root {
    --page: #f1f1f1;
    --brand-blue: #3f7297;
    --brand-blue-text: #2f5f8a;
    --card-light: #e9e9e9;
    --ink-dark: #4a4a4a;
    --ink-mid: #555555;
    --ink-tag: #333333;
    --paper: #f4f4f4;
  }
  * { margin: 0; padding: 0; box-sizing: border-box; }
  html, body { width: 1200px; height: 782px; overflow: hidden; }
  body {
    position: relative;
    background: var(--page);
    font-family: "Arimo", Helvetica, Arial, sans-serif;
  }
  .card { position: absolute; border-radius: 18px; box-shadow: 0 3px 8px rgba(0,0,0,.18); }

  /* Back of card */
  .card-back {
    left: 133px; top: 340px; width: 553px; height: 311px;
    background: var(--brand-blue);
  }
  .back-mark {
    position: absolute; left: 40px; top: 87px;
    width: 145px; height: 136px; border-radius: 12px;
    background: var(--paper);
  }
  .offerings {
    position: absolute; left: 397px; top: 295px;
    width: 290px; height: 140px;
    transform-origin: top left; transform: rotate(-90deg);
    color: var(--paper); font-size: 12.5px; line-height: 23.5px;
    list-style: none; white-space: nowrap;
  }
  .offerings-title { font-size: 14px; letter-spacing: .2px; }
  .offerings-title b { font-weight: 700; }
  .offering { display: flex; align-items: center; gap: 6px; }
  .offering svg { flex: none; transform: rotate(90deg); }
  .offering b { font-weight: 700; }

  /* Front of card */
  .card-front {
    left: 710px; top: 85px; width: 326px; height: 567px;
    background: var(--card-light);
  }
  .brand { position: absolute; left: 29px; top: 33px; display: flex; align-items: flex-start; gap: 12px; }
  .brand-square { width: 61px; height: 64px; background: var(--brand-blue); }
  .brand-name { font-size: 22px; font-weight: 700; color: var(--brand-blue-text); line-height: 1; margin-top: 9px; }
  .tagline {
    position: absolute; left: 111px; top: 69px;
    font-size: 12.5px; font-weight: 700; color: var(--ink-tag); letter-spacing: -.1px;
  }
  .contact { position: absolute; left: 0; right: 0; top: 412px; text-align: center; }
  .person { font-size: 24px; font-weight: 700; color: var(--ink-dark); line-height: 1.1; }
  .role { font-size: 14.5px; color: var(--brand-blue-text); margin-top: 3px; }
  .contact-icons { display: flex; justify-content: center; gap: 5px; margin-top: 13px; }
  .contact-lines { margin-top: 14px; font-size: 14px; line-height: 17.5px; color: var(--ink-mid); }
</style>
</head>
<body>
  <section class="card card-back">
    <div class="back-mark"></div>
    <ul class="offerings">
      <li class="offerings-title"><b>BROOKFIELD</b> VENTURES OFFERINGS</li>
      <li class="offering"><svg width="12" height="12" viewBox="0 0 12 12"><circle cx="6" cy="6" r="6" fill="#f4f4f4"/><rect x="3.5" y="3" width="5" height="6" fill="#3f7297"/></svg><span><b>Concepts:</b> Thought leadership white papers</span></li>
      <li class="offering"><svg width="12" height="12" viewBox="0 0 12 12"><circle cx="6" cy="6" r="6" fill="#f4f4f4"/><path d="M3 8 L6 3 L9 8 Z" fill="#3f7297"/></svg><span><b>Curriculum:</b> Short courses on strategy</span></li>
      <li class="offering"><svg width="12" height="12" viewBox="0 0 12 12"><circle cx="6" cy="6" r="6" fill="#f4f4f4"/><circle cx="6" cy="6" r="2.5" fill="#3f7297"/></svg><span><b>Coaching:</b> Building your strategic leadership</span></li>
      <li class="offering"><svg width="12" height="12" viewBox="0 0 12 12"><circle cx="6" cy="6" r="6" fill="#f4f4f4"/><circle cx="4" cy="7.5" r="1.3" fill="#3f7297"/><circle cx="8" cy="7.5" r="1.3" fill="#3f7297"/><circle cx="6" cy="4" r="1.3" fill="#3f7297"/></svg><span><b>Consulting:</b> Developing your strategic future</span></li>
      <li class="offering"><svg width="12" height="12" viewBox="0 0 12 12"><circle cx="6" cy="6" r="6" fill="#f4f4f4"/><path d="M3.5 8.5 V5 M6 8.5 V3.5 M8.5 8.5 V6" stroke="#3f7297" stroke-width="1.5"/></svg><span><b>ScoreCard:</b> Balanced ScoreCard and software</span></li>
    </ul>
  </section>

  <section class="card card-front">
    <div class="brand">
      <div class="brand-square"></div>
      <span class="brand-name">BrookfieldVentures</span>
    </div>
    <p class="tagline">Clear Vision - Lasting Results</p>
    <div class="contact">
      <p class="person">Dana Whitlow, PhD</p>
      <p class="role">Managing Director</p>
      <div class="contact-icons">
        <svg width="11" height="11" viewBox="0 0 12 12"><path d="M3 1 L5 3.5 L4 5 Q5.5 7.5 7 8 L8.5 7 L11 9 L9.5 11 Q4 10.5 1 3 Z" fill="#2f5f8a"/></svg>
        <svg width="12" height="11" viewBox="0 0 12 10"><rect x="1" y="1.5" width="10" height="7" fill="none" stroke="#2f5f8a" stroke-width="1.2"/><path d="M1 1.5 L6 5.5 L11 1.5" fill="none" stroke="#2f5f8a" stroke-width="1.2"/></svg>
        <svg width="11" height="11" viewBox="0 0 12 12"><circle cx="6" cy="6" r="5" fill="none" stroke="#2f5f8a" stroke-width="1.1"/><ellipse cx="6" cy="6" rx="2.2" ry="5" fill="none" stroke="#2f5f8a" stroke-width="1"/><path d="M1 6 H11" stroke="#2f5f8a" stroke-width="1"/></svg>
      </div>
      <div class="contact-lines">
        <p>555-014-2287</p>
        <p>Dana@BrookfieldVentures.com</p>
        <p>www.BrookfieldVentures.com</p>
      </div>
    </div>
  </section>
</body>
</html>
```